Corvelle Kids Expo Flyer

I'm looking to redesign my flyer. It should be easy to ready, eye-catching and kid friendly. I attached the flyer from last year. You can see all the deatils on my website www.corvellekidsexpo.com
I would need layered .psd file and fonts.

```html
<!DOCTYPE html>
<html lang="en">
<head>
<meta charset="utf-8">
<title>Corvelle Kids Expo Flyer</title>
<link rel="stylesheet" href="https://fonts.googleapis.com/css2?family=Roboto+Condensed:wght@400;700&family=Lato:wght@400;700&family=Roboto:wght@500;700&display=swap">
<style>
  :root {
    --cyan: #5bc6e0;
    --cyan-dark: #2f93ab;
    --teal-shadow: #1f6f80;
    --red: #e8262c;
    --ink: #2b2b2b;
    --grey-text: #3d3d3d;
    --bullet: #f05a28;
    --paper: #ffffff;
    --backdrop: #e6e6e6;
    --footer-ink: #203040;
  }
  * { margin: 0; padding: 0; box-sizing: border-box; }
  html, body { width: 900px; height: 1200px; overflow: hidden; background: var(--backdrop); }
  .flyer {
    position: absolute; left: 50px; top: 48px; width: 800px; height: 1112px;
    background: var(--paper); overflow: hidden;
    box-shadow: 0 4px 18px rgba(0,0,0,.25);
  }
  .flyer-art { position: absolute; left: 0; top: 0; }

  .brand-box {
    position: absolute; left: 53px; top: 59px; width: 285px; height: 145px;
    border: 5px solid var(--cyan); background: var(--paper);
    display: flex; align-items: center; justify-content: center; gap: 10px;
  }
  .brand-box .brand-mark { width: 16px; height: 16px; background: var(--cyan-dark); flex: none; }
  .brand-box .brand-name {
    font-family: "Roboto Condensed", sans-serif; font-weight: 700; font-size: 27px;
    color: var(--cyan-dark); text-transform: uppercase; line-height: 1; white-space: nowrap;
  }

  .headline p {
    position: absolute; left: 15px; width: 380px; text-align: center;
    white-space: nowrap; line-height: 1; font-family: "Roboto Condensed", sans-serif; font-weight: 700;
  }
  .headline .edition { top: 231px; font-size: 68px; color: var(--red); }
  .headline .event-name { top: 300px; font-family: "Roboto", sans-serif; font-size: 26px; color: var(--ink); letter-spacing: .3px; }
  .headline .weekday { top: 338px; font-size: 96px; color: var(--ink); letter-spacing: -1px; }
  .headline .date { top: 434px; font-size: 40px; color: var(--cyan); }
  .headline .hours { top: 482px; font-size: 56px; color: #111; }

  .activities { position: absolute; top: 594px; list-style: none; font-family: "Lato", sans-serif; font-weight: 700; font-size: 16px; color: var(--grey-text); text-transform: uppercase; }
  .activities.col-a { left: 40px; width: 210px; }
  .activities.col-b { left: 280px; width: 210px; }
  .activities li { position: relative; padding-left: 21px; line-height: 20px; margin-bottom: 6px; }
  .activities li::before { content: ""; position: absolute; left: 0; top: 7px; width: 6px; height: 6px; border-radius: 50%; background: var(--bullet); }

  .venue-tag { position: absolute; left: 44px; top: 810px; }
  .venue-card {
    position: absolute; left: 62px; top: 824px; width: 318px; height: 84px; background: var(--paper);
    box-shadow: 0 3px 8px rgba(0,0,0,.2); text-align: center; font-family: "Roboto", sans-serif; font-size: 21px; font-weight: 500;
    padding-top: 14px; line-height: 27px; white-space: nowrap;
  }
  .venue-card .venue-name { color: var(--red); font-weight: 700; }
  .venue-card .venue-address { color: var(--ink); }

  .prices { position: absolute; left: 60px; top: 938px; width: 300px; list-style: none; text-align: center; font-family: "Roboto", sans-serif; font-weight: 700; font-size: 17px; }
  .prices li { line-height: 27px; color: var(--red); text-transform: uppercase; white-space: nowrap; }
  .prices li::before { content: "\2022"; color: var(--cyan); margin-right: 8px; }
  .prices .price { color: #111; }

  .contact-band {
    position: absolute; left: 0; top: 1032px; width: 800px; height: 80px; background: var(--cyan);
    font-family: "Roboto", sans-serif; font-weight: 700; font-size: 20px; color: #fff;
  }
  .contact-band .website { position: absolute; left: 45px; top: 27px; display: flex; align-items: center; gap: 12px; color: var(--footer-ink); }
  .contact-band .phone { position: absolute; left: 494px; top: 27px; }
  .contact-band .phone-number { font-weight: 500; }
</style>
</head>
<body>
<main class="flyer">
  <svg class="flyer-art" viewBox="0 0 800 1112" width="800" height="1112">
    <defs>
      <linearGradient id="crowd-tone" x1="0" y1="0" x2="1" y2="1">
        <stop offset="0" stop-color="#5aa9bb"/>
        <stop offset=".6" stop-color="#2f8599"/>
        <stop offset="1" stop-color="#1f6577"/>
      </linearGradient>
      <linearGradient id="kids-tone" x1="0" y1="0" x2="1" y2="0">
        <stop offset="0" stop-color="#d9a98b"/>
        <stop offset=".5" stop-color="#c98a7a"/>
        <stop offset="1" stop-color="#b97994"/>
      </linearGradient>
      <radialGradient id="blocks-tone" cx=".5" cy=".55" r=".6">
        <stop offset="0" stop-color="#f4d15a"/>
        <stop offset=".55" stop-color="#e8765a"/>
        <stop offset="1" stop-color="#f7f7f7"/>
      </radialGradient>
      <clipPath id="lower-half">
        <rect x="0" y="440" width="800" height="600"/>
      </clipPath>
    </defs>
    <rect class="top-band" x="0" y="0" width="800" height="30" fill="var(--cyan)"/>
    <path class="accent-curve" d="M 440 30 C 600 330, 600 700, 350 1032" fill="none" stroke="var(--red)" stroke-width="10"/>
    <path class="crowd-photo" role="img" aria-label="Photo area: children cheering and dancing at a performance, teal toned"
          clip-path="url(#lower-half)"
          d="M 455 30 C 615 330, 615 700, 365 1032 L 800 1032 L 800 30 Z" fill="url(#crowd-tone)"/>
    <rect class="kids-photo" role="img" aria-label="Photo area: group of smiling children lying together on the floor"
          x="430" y="867" width="370" height="165" fill="url(#kids-tone)"/>
    <circle class="photo-ring-outer" cx="595" cy="252" r="216" fill="var(--cyan)"/>
    <circle class="photo-ring-inner" cx="595" cy="252" r="208" fill="var(--paper)"/>
    <circle class="blocks-photo" role="img" aria-label="Photo area: children sitting on colourful foam letter and number blocks"
            cx="595" cy="252" r="198" fill="url(#blocks-tone)"/>
  </svg>

  <div class="brand-box">
    <span class="brand-mark"></span>
    <span class="brand-name">Corvelle Kids Expo</span>
  </div>

  <header class="headline">
    <p class="edition">4TH ANNUAL</p>
    <p class="event-name">CORVELLE KIDS EXPO</p>
    <p class="weekday">SUNDAY</p>
    <p class="date">APRIL 26TH, 2015</p>
    <p class="hours">11am-4pm</p>
  </header>

  <ul class="activities col-a">
    <li>Amber Alert Registration</li>
    <li>Train Ride</li>
    <li>Live Animal Games</li>
    <li>Prize</li>
    <li>Magic</li>
    <li>Face Painting</li>
  </ul>
  <ul class="activities col-b">
    <li>Balloon Art</li>
    <li>Caricature</li>
    <li>Performance Arts</li>
    <li>Bounce Houses</li>
    <li>Special Guest Appearances</li>
    <li>Sand Art</li>
  </ul>

  <svg class="venue-tag" viewBox="0 0 360 110" width="360" height="110" aria-hidden="true">
    <polygon points="0,0 340,10 360,100 20,110" fill="var(--teal-shadow)"/>
    <polygon points="0,0 18,16 20,110" fill="var(--cyan-dark)"/>
  </svg>
  <div class="venue-card">
    <p class="venue-name">Brightfield sports demo</p>
    <p class="venue-address">48 maple ridge lane</p>
  </div>

  <ul class="prices">
    <li>Ages 12 and over: <span class="price">$10</span></li>
    <li>Ages 3-11: <span class="price">$7</span></li>
    <li>Ages 2 and under: <span class="price">FREE</span></li>
  </ul>

  <footer class="contact-band">
    <p class="website">
      <svg width="20" height="20" viewBox="0 0 20 20" aria-hidden="true">
        <g fill="none" stroke="var(--footer-ink)" stroke-width="1.6">
          <circle cx="10" cy="10" r="8.5"/>
          <ellipse cx="10" cy="10" rx="3.8" ry="8.5"/>
          <line x1="1.5" y1="10" x2="18.5" y2="10"/>
        </g>
      </svg>
      www.corvellekidsexpo.com
    </p>
    <p class="phone">CALL US: <span class="phone-number">555-014-2290</span></p>
  </footer>
</main>
</body>
</html>
```